Business card design reauest

2 sided. White on both sides

Martin Oakhurst

Ho Chi Minh, Vietnam

Cell Phone / Whatsapp/ Wechat/Zalo
1-555-382-7194
Moakhurst@kvpartsline.vn
Www.kvpartsline.vn
Www.kvpartsline.com

Industry/Entity Type

Sofa and furniture and kitchen

Contact Information for Business Card

2 sided. White on both sides Martin Oakhurst Ho Chi Minh, Vietnam Cell Phone / Whatsapp/ Wechat/Zalo 1-555-382-7194 Moakhurst@kvpartsline.vn Www.kvpartsline.vn Www.kvpartsline.com

```html
<!DOCTYPE html>
<html lang="en">
<head>
<meta charset="utf-8">
<title>KV Parts Line – Business Card</title>
<link rel="stylesheet" href="https://fonts.googleapis.com/css2?family=Lexend:wght@400;700&display=swap">
<style>
  :root {
    --backdrop: #b6b49f;
    --card: #ffffff;
    --brand-green: #009846;
    --ink: #111111;
    --grey-light: #f2f2f2;
    --grey-mid: #e0e0e0;
  }
  * { box-sizing: border-box; margin: 0; padding: 0; }
  html, body {
    width: 764px;
    height: 1200px;
    overflow: hidden;
    background: var(--backdrop);
  }
  .canvas {
    position: relative;
    width: 764px;
    height: 1200px;
    font-family: "Lexend", sans-serif;
  }
  .card {
    position: absolute;
    left: 132px;
    width: 500px;
    height: 324px;
    background: var(--card);
    overflow: hidden;
  }
  .card--front { top: 241px; }
  .card--back { top: 634px; }

  .card__swoop {
    position: absolute;
    inset: 0;
    width: 500px;
    height: 324px;
  }
  .swoop__light { fill: var(--grey-light); }
  .swoop__mid { fill: var(--grey-mid); }
  .swoop__green { fill: var(--brand-green); }

  .holder__name {
    position: absolute;
    left: 36px;
    top: 64px;
    font-size: 43px;
    font-weight: 700;
    letter-spacing: -0.5px;
    color: var(--brand-green);
    white-space: nowrap;
    line-height: 1;
  }
  .holder__city {
    position: absolute;
    left: 37px;
    top: 121px;
    font-size: 16px;
    font-weight: 400;
    color: var(--ink);
    line-height: 1;
  }
  .contact {
    position: absolute;
    left: 37px;
    top: 160px;
    list-style: none;
    font-size: 13.5px;
    color: var(--ink);
    line-height: 1;
  }
  .contact__item { height: 25px; display: flex; align-items: center; }
  .contact__item--phone { height: 28px; font-size: 14px; }
  .contact__icon { width: 14px; height: 14px; margin-right: 7px; }

  .brand {
    position: absolute;
    color: var(--brand-green);
    font-weight: 400;
    white-space: nowrap;
    text-align: center;
    line-height: 1;
  }
  .brand--front {
    left: 336px;
    top: 276px;
    width: 140px;
    font-size: 14px;
    letter-spacing: 1px;
  }
  .brand--back {
    left: 0;
    top: 148px;
    width: 500px;
    font-size: 28px;
    letter-spacing: 2px;
  }
</style>
</head>
<body>
<main class="canvas">
  <section class="card card--front" aria-label="Business card front">
    <svg class="card__swoop" viewBox="0 0 500 324" aria-hidden="true">
      <path class="swoop__light" d="M343,0 C370,45 386,95 382,145 L400,140 C450,102 482,60 491,0 Z"/>
      <path class="swoop__mid" d="M437,0 C428,55 410,100 384,143 L400,140 C450,102 482,60 491,0 Z"/>
      <path class="swoop__green" d="M251,324 C262,240 320,190 382,146 C445,100 482,60 491,0 C484,72 448,118 390,160 C325,208 272,255 251,324 Z"/>
    </svg>

    <h1 class="holder__name">Martin Oakhurst</h1>
    <p class="holder__city">Ho Chi Minh, Vietnam</p>

    <ul class="contact">
      <li class="contact__item contact__item--phone">
        <svg class="contact__icon" viewBox="0 0 24 24" aria-hidden="true">
          <circle cx="12" cy="12" r="12" fill="#111"/>
          <path fill="#fff" d="M8.2 6.2c.4-.3 1-.2 1.3.2l1.3 2c.3.4.2.9-.1 1.2l-.8.7c.6 1.4 1.6 2.5 3 3.2l.7-.8c.3-.3.8-.4 1.2-.1l2 1.3c.4.3.5.9.2 1.3l-.7 1c-.5.6-1.3.9-2 .6-3.3-1.2-5.8-3.7-7-7-.3-.7 0-1.5.6-2z"/>
        </svg>
        <span>1-555-382-7194</span>
      </li>
      <li class="contact__item">Moakhurst@kvpartsline.vn</li>
      <li class="contact__item">www.kvpartsline.vn</li>
      <li class="contact__item">www.kvpartsline.com</li>
    </ul>

    <p class="brand brand--front">KV PARTS LINE</p>
  </section>

  <section class="card card--back" aria-label="Business card back">
    <p class="brand brand--back">KV PARTS LINE</p>
  </section>
</main>
</body>
</html>
```